Edit current business card design

Need business card design where Business Name, Logo, Address, phone and fax, website address are permanent.Need to be able to add and edit employee name and email address.

Business

```html
<!DOCTYPE html>
<html lang="en">
<head>
<meta charset="utf-8">
<title>Marlow Tax &amp; Accounting – Business Card</title>
<link href="https://fonts.googleapis.com/css2?family=Questrial&display=swap" rel="stylesheet">
<style>
  :root{
    --orange:#ef5a24;
    --ink:#333333;
    --card-white:#ffffff;
    --card-dark:#262626;
    --card-dark-2:#353535;
    --backdrop:#e9e6e2;
    --rule:#3a3a3a;
    --light-text:#f2f2f2;
  }
  *{box-sizing:border-box;margin:0;padding:0}
  html,body{width:1200px;height:900px;overflow:hidden}
  body{
    background:var(--backdrop);
    font-family:"Questrial",sans-serif;
    color:var(--ink);
    position:relative;
  }
  .card{
    position:absolute;
    left:285px;
    width:630px;height:360px;
    border-radius:18px;
    box-shadow:0 10px 28px rgba(0,0,0,.22);
    overflow:hidden;
  }

  /* Back side */
  .card-back{
    top:50px;
    background:linear-gradient(160deg,var(--card-dark-2),var(--card-dark));
    color:var(--light-text);
  }
  .services{position:absolute;left:42px;top:40px}
  .services-title{color:var(--orange);font-size:20px;font-weight:400;letter-spacing:1px;margin-bottom:4px}
  .service-list{list-style:none}
  .service-list li{display:flex;align-items:center;gap:10px;font-size:19px;line-height:31px}
  .tick{width:17px;height:17px;flex:none}
  .tagline{margin-top:10px;font-size:19px;line-height:24px}
  .tagline-lead{color:var(--orange)}
  .brand-back{position:absolute;right:38px;top:208px}

  /* Brand lockup */
  .brand{display:flex;align-items:center;gap:9px}
  .brand-square{width:18px;height:18px;background:var(--orange);flex:none}
  .brand-name{font-size:20px;color:var(--ink)}
  .card-back .brand-name{color:var(--light-text)}

  /* Front side */
  .card-front{top:490px;background:var(--card-white)}
  .brand-front{position:absolute;right:36px;top:36px}
  .brand-front .brand-square{width:20px;height:20px}
  .brand-front .brand-name{font-size:25px}
  .top-rule{position:absolute;left:250px;right:36px;top:100px;height:2px;background:var(--rule)}
  .person{position:absolute;left:40px;top:126px;padding-left:18px;border-left:7px solid var(--orange)}
  .person-name{font-size:34px;font-weight:400;line-height:38px;color:var(--ink)}
  .person-credentials{font-size:20px;color:var(--orange);letter-spacing:.5px}
  .mid-rule{position:absolute;left:40px;right:36px;top:208px;height:2px;background:var(--rule)}
  .contact{list-style:none;position:absolute}
  .contact-left{left:40px;top:220px}
  .contact-right{left:350px;top:126px}
  .contact li{display:flex;align-items:center;gap:12px;font-size:20px;line-height:32px;margin-bottom:2px}
  .icon{width:24px;height:24px;flex:none}
</style>
</head>
<body>

<section class="card card-back" aria-label="Card back">
  <div class="services">
    <h2 class="services-title">SERVICES</h2>
    <ul class="service-list">
      <li><svg class="tick" viewBox="0 0 18 18"><rect x="1" y="3" width="13" height="13" fill="none" stroke="#ef5a24" stroke-width="2"/><path d="M4 9l4 4 9-11" fill="none" stroke="#ef5a24" stroke-width="2.6"/></svg>Tax planning &amp; preparation for business &amp; individuals</li>
      <li><svg class="tick" viewBox="0 0 18 18"><rect x="1" y="3" width="13" height="13" fill="none" stroke="#ef5a24" stroke-width="2"/><path d="M4 9l4 4 9-11" fill="none" stroke="#ef5a24" stroke-width="2.6"/></svg>Tax problem resolutions</li>
      <li><svg class="tick" viewBox="0 0 18 18"><rect x="1" y="3" width="13" height="13" fill="none" stroke="#ef5a24" stroke-width="2"/><path d="M4 9l4 4 9-11" fill="none" stroke="#ef5a24" stroke-width="2.6"/></svg>Bookkeeping and Payroll Services</li>
      <li><svg class="tick" viewBox="0 0 18 18"><rect x="1" y="3" width="13" height="13" fill="none" stroke="#ef5a24" stroke-width="2"/><path d="M4 9l4 4 9-11" fill="none" stroke="#ef5a24" stroke-width="2.6"/></svg>Incorporation &amp; new business advisor</li>
      <li><svg class="tick" viewBox="0 0 18 18"><rect x="1" y="3" width="13" height="13" fill="none" stroke="#ef5a24" stroke-width="2"/><path d="M4 9l4 4 9-11" fill="none" stroke="#ef5a24" stroke-width="2.6"/></svg>Bookkeeping support &amp; training</li>
      <li><svg class="tick" viewBox="0 0 18 18"><rect x="1" y="3" width="13" height="13" fill="none" stroke="#ef5a24" stroke-width="2"/><path d="M4 9l4 4 9-11" fill="none" stroke="#ef5a24" stroke-width="2.6"/></svg>And more....</li>
    </ul>
    <p class="tagline"><span class="tagline-lead">Helping our Clients</span><br>Keep More of What They Make......</p>
  </div>
  <div class="brand brand-back"><span class="brand-square"></span><span class="brand-name">Marlow Tax &amp; Accounting</span></div>
</section>

<section class="card card-front" aria-label="Card front">
  <div class="brand brand-front"><span class="brand-square"></span><span class="brand-name">Marlow Tax &amp; Accounting</span></div>
  <div class="top-rule"></div>

  <div class="person">
    <h1 class="person-name">Dana Keller</h1>
    <p class="person-credentials">EA,ATA,ATP</p>
  </div>

  <ul class="contact contact-right">
    <li><svg class="icon" viewBox="0 0 26 26"><rect width="26" height="26" rx="5" fill="#ef5a24"/><rect x="8" y="5" width="10" height="6" fill="#fff"/><rect x="5" y="11" width="16" height="9" rx="1.5" fill="#fff"/><rect x="8" y="14" width="10" height="2" fill="#ef5a24"/></svg>(555) 208 5510</li>
    <li><svg class="icon" viewBox="0 0 26 26"><rect width="26" height="26" rx="5" fill="#ef5a24"/><circle cx="13" cy="13" r="8" fill="none" stroke="#fff" stroke-width="1.6"/><ellipse cx="13" cy="13" rx="3.5" ry="8" fill="none" stroke="#fff" stroke-width="1.4"/><path d="M5 13h16M6.5 9h13M6.5 17h13" stroke="#fff" stroke-width="1.2"/></svg>www.marlowtax.com</li>
  </ul>

  <div class="mid-rule"></div>

  <ul class="contact contact-left">
    <li><svg class="icon" viewBox="0 0 26 26"><rect width="26" height="26" rx="5" fill="#ef5a24"/><path d="M5 10q8-6 16 0v2h-4v-2H9v2H5z" fill="#fff"/><rect x="7" y="13" width="12" height="7" rx="1.5" fill="#fff"/></svg>(555) 208 1147</li>
    <li><svg class="icon" viewBox="0 0 26 26"><rect width="26" height="26" rx="5" fill="#ef5a24"/><rect x="5" y="8" width="16" height="11" fill="#fff"/><path d="M5 8l8 6 8-6" fill="none" stroke="#ef5a24" stroke-width="1.5"/></svg>dana@marlowtax.com</li>
    <li><svg class="icon" viewBox="0 0 26 26"><rect width="26" height="26" rx="5" fill="#ef5a24"/><path d="M13 21s-6-6.5-6-10.5a6 6 0 0 1 12 0C19 14.5 13 21 13 21z" fill="#fff"/><circle cx="13" cy="10.5" r="2.3" fill="#ef5a24"/></svg>12 Linden Ct Unit 4 Brookvale, OR 97000</li>
  </ul>
</section>

</body>
</html>
```